Room Hire at The Willowmere Wellbeing & Talking House to encourage therapists to hire rooms from us

An A4 page for magazine printing and use to send online as well.

We want to attract therapists to come and hire our beautiful rooms. We have a soft green, cream and brown colour theme and a professional, warm, elegant style (we hope)
I've uploaded the previous advert we had done through art bazaar which was aimed at attracting therapy clients.

Target Market(s)

psychotherapists and physical therapists searching to hire consulting rooms

Industry/Entity Type

Font styles to use
Serif
Sans Serif
Script
Other font styles liked:
• Good Vibes

Colors
cadf82
abd037
9bcb3c
fdf9ce
fff3d1

Requirements
Must have
• Please include this text
• Website address
• Contact email address
• "The rooms are available to hire all day into the evenings and at weekends.
• There are 8 rooms, all suitable for Couples work, Individual Counselling or Supervision sessions. Some rooms are designed to be used by physical therapists as well. One of them is large enough to use for Family Therapy, to hold groups or to run Training Sessions for approximately fourteen people."
• The colour scheme to harmonise with our website theme colours and fonts - Colour RGA numbers
• Brown
• Red 65
• Green 53
• Blue 53
• Light green
• Red 129
• Green 157
• Blue 115
• www.wmth-harbridge.example.co.uk.
• Scrolling writing is Good Vibes by Plinko
• Be warm, calm, welcoming, professional styling, striking.
Nice to have
• Pictures of our rooms if we can provide enough quality for printing
Should not have
• Pictures of people touching each other.
• Not be too busy or angular

```html
<!DOCTYPE html>
<html lang="en">
<head>
<meta charset="utf-8">
<title>Room Hire – The Willowmere Wellbeing &amp; Talking House</title>
<link href="https://fonts.googleapis.com/css2?family=Great+Vibes&family=Lato:wght@400;700&family=Roboto+Condensed:wght@700&display=swap" rel="stylesheet">
<style>
  :root{
    --page-bg:#e6e6e4;
    --paper:#ffffff;
    --paper-shade:#f2f2f2;
    --green:#9bcb3c;
    --green-bright:#abd037;
    --green-soft:#cadf82;
    --brown:#413535;
    --ink:#1e1e1e;
    --text:#333333;
    --room-warm:#d9c08f;
    --room-cream:#efe2c2;
    --room-wood:#a9814f;
  }
  *{box-sizing:border-box;margin:0;padding:0}
  html,body{width:1200px;height:1024px;overflow:hidden;background:var(--page-bg)}
  .flyer{
    position:absolute;left:250px;top:20px;width:700px;height:984px;
    background:linear-gradient(180deg,var(--paper) 60%,var(--paper-shade));
    box-shadow:0 6px 24px rgba(0,0,0,.18);
    overflow:hidden;
    font-family:"Lato",sans-serif;
  }
  .hero-art{position:absolute;left:0;top:0;width:700px;height:740px}
  .headline{position:absolute;left:48px;top:352px;width:320px}
  .headline-line{
    font-family:"Great Vibes",cursive;font-size:58px;line-height:50px;
    color:var(--ink);font-weight:400;
  }
  .headline-line--accent{color:var(--green-bright);font-size:60px}
  .headline-sub{
    margin-top:6px;font-family:"Roboto Condensed",sans-serif;font-weight:700;
    font-size:14px;letter-spacing:.1px;color:var(--ink);white-space:nowrap;
  }
  .intro{
    position:absolute;left:32px;top:788px;width:650px;
    font-size:13.4px;line-height:17px;color:var(--text);
  }
  .intro strong{color:var(--ink)}
  .brand{
    position:absolute;left:20px;top:880px;width:220px;
    display:flex;flex-direction:column;align-items:center;gap:10px;
  }
  .brand-dot{width:26px;height:26px;border-radius:50%;background:var(--green)}
  .brand-name{
    font-size:14px;line-height:17px;text-align:center;color:var(--brown);font-weight:400;
  }
  .contact{position:absolute;font-style:normal;color:var(--ink);font-weight:700}
  .contact-item{display:flex;align-items:flex-start;gap:6px}
  .contact-item svg{flex:none;margin-top:2px}
  .contact--direct{left:250px;top:908px;width:245px;font-size:11px;line-height:14px}
  .contact--direct .contact-item{margin-bottom:9px;white-space:nowrap}
  .contact--direct .contact-phone{font-size:14px;line-height:16px}
  .contact--web{left:506px;top:902px;width:184px;font-size:10.5px;line-height:14px}
  .contact--web .contact-item{margin-bottom:6px}
  .contact--web .contact-url{white-space:nowrap}
  .footer-band{position:absolute;left:0;bottom:0;width:700px;height:18px;background:var(--green)}
</style>
</head>
<body>
<main class="flyer">
  <svg class="hero-art" viewBox="0 0 700 740">
    <defs>
      <linearGradient id="roomTop" x1="0" y1="0" x2="1" y2="1">
        <stop offset="0" stop-color="#efe2c2"/>
        <stop offset=".5" stop-color="#d9c08f"/>
        <stop offset="1" stop-color="#a9814f"/>
      </linearGradient>
      <linearGradient id="roomLower" x1="0" y1="0" x2="0" y2="1">
        <stop offset="0" stop-color="#f3ead6"/>
        <stop offset=".6" stop-color="#e4d6b6"/>
        <stop offset="1" stop-color="#7a6a5c"/>
      </linearGradient>
    </defs>
    <path role="img" aria-label="Photo of a consulting room with a cream tub armchair, wooden sideboard, plants and a window"
          fill="url(#roomTop)"
          d="M0,0 H700 V215 C600,235 510,280 455,325 C360,285 210,280 0,338 Z"/>
    <path fill="none" stroke="var(--green-bright)" stroke-width="7" stroke-linecap="round"
          d="M0,418 C70,340 250,270 458,328"/>
    <path role="img" aria-label="Photo of a therapy room with two cream armchairs facing each other by a curtained door"
          fill="url(#roomLower)"
          d="M148,640 C300,600 400,385 500,318 C580,268 650,225 700,212 V678 C650,692 580,712 480,716 C380,720 280,655 148,640 Z"/>
    <path fill="none" stroke="var(--green-bright)" stroke-width="7" stroke-linecap="round"
          d="M148,640 C300,600 400,385 500,318 C580,268 650,225 700,210"/>
    <path fill="none" stroke="var(--green-bright)" stroke-width="7" stroke-linecap="round"
          d="M148,640 C280,650 380,722 480,718 C580,714 650,694 700,680"/>
  </svg>

  <header class="headline">
    <h1 class="headline-line">The rooms are</h1>
    <p class="headline-line headline-line--accent">Available to hire</p>
    <p class="headline-sub">ALL DAY INTO THE EVENINGS AND AT WEEKENDS</p>
  </header>

  <p class="intro">There are <strong>8 rooms</strong>, all suitable for Couples work, Individual Counselling or Supervision sessions. Some rooms are designed to be used by physical therapists as well. One of them is large enough to use for Family Therapy, to hold groups or to run Training Sessions for approximately fourteen people.</p>

  <div class="brand">
    <span class="brand-dot"></span>
    <span class="brand-name">The Willowmere Wellbeing<br>&amp; Talking House</span>
  </div>

  <address class="contact contact--direct">
    <div class="contact-item contact-phone">
      <svg width="12" height="12" viewBox="0 0 24 24"><path fill="var(--ink)" d="M6.6 10.8a15 15 0 0 0 6.6 6.6l2.2-2.2a1 1 0 0 1 1-.25 11 11 0 0 0 3.6.6 1 1 0 0 1 1 1V20a1 1 0 0 1-1 1A17 17 0 0 1 3 4a1 1 0 0 1 1-1h3.5a1 1 0 0 1 1 1 11 11 0 0 0 .6 3.6 1 1 0 0 1-.25 1z"/></svg>
      <span>01632 960482</span>
    </div>
    <div class="contact-item">
      <svg width="11" height="11" viewBox="0 0 24 24"><rect x="2" y="5" width="20" height="14" rx="2" fill="var(--ink)"/><path d="M3 6l9 7 9-7" fill="none" stroke="#fff" stroke-width="2"/></svg>
      <span>rosalind@wmth-harbridge.example.co.uk</span>
    </div>
  </address>

  <address class="contact contact--web">
    <div class="contact-item contact-url">
      <svg width="10" height="10" viewBox="0 0 24 24"><circle cx="12" cy="12" r="10" fill="none" stroke="var(--ink)" stroke-width="2.4"/><path d="M2 12h20M12 2c4 4 4 16 0 20M12 2c-4 4-4 16 0 20" fill="none" stroke="var(--ink)" stroke-width="2"/></svg>
      <span>www.wmth-harbridge.example.co.uk</span>
    </div>
    <div class="contact-item">
      <svg width="10" height="10" viewBox="0 0 24 24"><path fill="var(--ink)" d="M12 2 2 11h3v10h5v-6h4v6h5V11h3z"/></svg>
      <span>The Willowmere Wellbeing &amp; Talking House, 14 Alder Lane, Harbridge, Wessex HB2 7QW</span>
    </div>
  </address>

  <div class="footer-band"></div>
</main>
</body>
</html>
```